The Copper Ladder

we require a classy business card design for a business coaching company that uses our current logo and the wording:

Front of card:

LOGO
Kyle Morrison
CEO
TEL: 1300 4 52918
FAX: 1300 5 52918
Mobile: 0412 638194
PO Box 917, Ferris Hollow, Brisbane, Qld 4127
e: kylem@copperladder.com.au
w: www.copperladder.com.au

Reverse side of the card:

Systematizing Businesses into Turnkey Operations
Strategic Business Plans
Sales & Marketing Programs
Sales Training & Business Coaching
Internet Marketing & Web Design

Here’s what our clients say:

“We grew from $396,000 to over $5million in 4 years and made KTS’s Rising Enterprises Roll 3 years running!” – Martin Greaves, Meridian Works

Target Market(s)

small to medium sized business owners in Australia

Industry/Entity Type

Business

Requirements
Must have
• standard business card size

```html
<!DOCTYPE html>
<html lang="en">
<head>
<meta charset="utf-8">
<title>The Copper Ladder – Business Card</title>
<link rel="stylesheet" href="https://fonts.googleapis.com/css2?family=Arimo:wght@400;700&family=Archivo+Black&display=swap">
<style>
  :root {
    --amber: #fbb62b;
    --amber-soft: rgba(251, 182, 43, 0);
    --ink: #111111;
    --outline: #5a3a00;
    --rule: #7b7bf0;
    --paper: #ffffff;
    --ghost: #b3b3b3;
  }
  html, body {
    margin: 0;
    padding: 0;
    width: 987px;
    height: 1200px;
    overflow: hidden;
    background: var(--paper);
  }
  .canvas {
    position: relative;
    width: 987px;
    height: 1200px;
    overflow: hidden;
  }
  .stage {
    position: absolute;
    top: 0;
    left: 0;
    width: 1050px;
    height: 1277px;
    transform: scale(0.94);
    transform-origin: 0 0;
    font-family: "Arimo", Arial, sans-serif;
    color: var(--ink);
  }
  .card {
    position: absolute;
    left: 0;
    width: 1050px;
    overflow: hidden;
    background: var(--paper);
  }
  .card--front { top: 0; height: 600px; border-bottom: 1px solid var(--rule); }
  .card--back { top: 675px; height: 602px; border-top: 1px solid var(--rule); }
  .card__backdrop { position: absolute; inset: 0; width: 100%; height: 100%; }

  .wordmark {
    position: absolute;
    left: 0;
    right: 0;
    text-align: center;
    font-family: "Arimo", Arial, sans-serif;
    font-weight: 700;
    letter-spacing: -1px;
    margin: 0;
  }
  .wordmark--front { top: 72px; font-size: 74px; color: var(--ink); }
  .wordmark--back { top: 1000px; font-size: 100px; color: var(--ghost); top: 420px; }

  .person {
    position: absolute;
    top: 255px;
    left: 0;
    right: 0;
    text-align: center;
  }
  .person__name {
    margin: 0;
    font-family: "Archivo Black", "Arial Black", sans-serif;
    font-size: 47px;
    line-height: 56px;
    color: var(--amber);
    -webkit-text-stroke: 1px var(--outline);
  }
  .person__role,
  .person__address {
    margin: 0;
    font-size: 22px;
    line-height: 30px;
  }
  .person__address { margin-top: 7px; }

  .contact {
    position: absolute;
    height: 30px;
    font-size: 22px;
    line-height: 30px;
  }
  .contact--left {
    left: 0;
    width: 390px;
    padding-left: 19px;
    box-sizing: border-box;
    background: linear-gradient(90deg, var(--amber) 0%, var(--amber) 40%, var(--amber-soft) 100%);
  }
  .contact--right {
    right: 0;
    width: 365px;
    padding-right: 17px;
    box-sizing: border-box;
    text-align: right;
    background: linear-gradient(270deg, var(--amber) 0%, var(--amber) 40%, var(--amber-soft) 100%);
  }
  .tagline-art {
    position: absolute;
    left: 355px;
    top: 466px;
    width: 340px;
    height: 108px;
    background: radial-gradient(ellipse at center, #e4e4e4 0%, #f6f6f6 60%, var(--paper) 100%);
  }

  .services {
    position: absolute;
    top: 33px;
    left: 0;
    right: 0;
    margin: 0;
    padding: 0;
    list-style: none;
    text-align: center;
    font-size: 22px;
  }
  .services li { height: 62.5px; line-height: 32px; }
</style>
</head>
<body>
<div class="canvas">
  <div class="stage">

    <section class="card card--front" aria-label="Card front">
      <svg class="card__backdrop" viewBox="0 0 1050 600" preserveAspectRatio="none" aria-hidden="true">
        <rect width="1050" height="600" fill="var(--amber)"/>
        <ellipse cx="525" cy="700" rx="600" ry="720" fill="var(--paper)"/>
        <rect x="0" y="440" width="1050" height="160" fill="var(--paper)"/>
      </svg>

      <p class="wordmark wordmark--front">The Copper Ladder</p>

      <div class="person">
        <h1 class="person__name">Kyle Morrison</h1>
        <p class="person__role">CEO</p>
        <p class="person__address">PO Box 917, Ferris Hollow<br>Brisbane, Qld 4127</p>
      </div>

      <div class="contact contact--left" style="top:466px">Tel:1300-4-52918</div>
      <div class="contact contact--left" style="top:508px">Fax: 1300-5-52918</div>
      <div class="contact contact--left" style="top:550px">Mobile: 0412-638194</div>

      <div class="tagline-art" role="img" aria-label="Hand-lettered tagline: marketing that's so effective it's like printing your own money, with a looping flourish"></div>

      <div class="contact contact--right" style="top:510px">kylem@copperladder.com.au</div>
      <div class="contact contact--right" style="top:552px">www.copperladder.com.au</div>
    </section>

    <section class="card card--back" aria-label="Card back">
      <svg class="card__backdrop" viewBox="0 0 1050 602" preserveAspectRatio="none" aria-hidden="true">
        <rect width="1050" height="602" fill="var(--amber)"/>
        <ellipse cx="525" cy="330" rx="590" ry="345" fill="var(--paper)"/>
        <rect x="0" y="300" width="1050" height="302" fill="var(--paper)"/>
      </svg>

      <ul class="services">
        <li>Systematizing Businesses into Turnkey Operations</li>
        <li>Strategic Business Plans</li>
        <li>Sales &amp; Marketing Programs</li>
        <li>Sales Training &amp; Business Coaching</li>
        <li>Internet Marketing &amp; Web Design</li>
      </ul>

      <p class="wordmark wordmark--back">The Copper Ladder</p>
    </section>

  </div>
</div>
</body>
</html>
```